Lorna Tess Tresses Fancy Business Card’s

I want my business cards to be elite, original and very classy. I want the business cards to match the colors of my logo and to match the design posted. I would love the design of the picture I posted

I want the card all white .
The dripping on the top of the card I want it to match the pink color in my logo that’s also posted .
I need my logo on the business card !
I need my Instagram- @lorna.tess.tresses__
And my phone number - 582 907 3365

Target Market(s)

My target market is young woman age 23 to older woman to the age of 65
I want both older and younger women to love my design . I don’t want any cheap looking business cards

Industry/Entity Type

Hair And Beauty

Contact Information for Business Card

Add my logo
Add my Instagram- @lorna.tess.tresses__
My number - 582 907 3365
My website- www.lornatesstresses.example

Font styles to use
Serif
Script

Colors
ffffff
e667a6
e34298

Requirements
Must have
• The business cards must have my logo, my number , my website, and my Instagram!
Nice to have
• Nice to have glitter words that match my logo
• The business cards must look classy and mature
• I want them to be very unique!!
Should not have
• Should not have any colors that doesn’t match my logo ! This is very important! Please

```html
<!DOCTYPE html>
<html lang="en">
<head>
<meta charset="utf-8">
<title>Lorna Tess Tresses — Business Card</title>
<link rel="stylesheet" href="https://fonts.googleapis.com/css2?family=Playfair+Display:wght@400&family=Roboto:wght@400&display=swap">
<style>
  :root {
    --backdrop: #1d1d1d;
    --card-white: #ffffff;
    --card-pink: #e34298;
    --pink-soft: #e667a6;
    --pink-deep: #c93185;
    --ink: #3a3a3a;
  }
  * { margin: 0; padding: 0; box-sizing: border-box; }
  html, body {
    width: 1200px;
    height: 1021px;
    overflow: hidden;
    background: var(--backdrop);
  }
  .sheet {
    position: relative;
    width: 1200px;
    height: 1021px;
    display: flex;
    justify-content: center;
    align-items: center;
    gap: 80px;
  }
  .card {
    position: relative;
    width: 400px;
    height: 700px;
    border-radius: 4px;
    display: flex;
    flex-direction: column;
    align-items: center;
  }
  .card--front { background: var(--card-pink); justify-content: center; }
  .card--back { background: var(--card-white); }

  .wordmark {
    font-family: "Playfair Display", serif;
    font-weight: 400;
    text-align: center;
    line-height: 1.05;
    font-size: 52px;
  }
  .card--front .wordmark { color: var(--pink-deep); }
  .card--back .wordmark { color: var(--card-pink); margin-top: 150px; }

  .contact {
    margin-top: auto;
    margin-bottom: 120px;
    display: flex;
    flex-direction: column;
    align-items: center;
    gap: 10px;
    font-family: "Roboto", sans-serif;
    color: var(--ink);
  }
  .contact__icons {
    display: flex;
    gap: 14px;
    align-items: center;
    margin-bottom: 6px;
  }
  .contact__icons svg { width: 20px; height: 20px; }
  .contact__line { font-size: 19px; letter-spacing: 0.2px; }
</style>
</head>
<body>
<main class="sheet">
  <section class="card card--front" aria-label="Card front">
    <p class="wordmark">Lorna<br>Tess<br>Tresses</p>
  </section>

  <section class="card card--back" aria-label="Card back">
    <p class="wordmark">Lorna<br>Tess<br>Tresses</p>

    <div class="contact">
      <div class="contact__icons">
        <svg viewBox="0 0 20 20" aria-label="Social handle">
          <rect x="3" y="3" width="14" height="14" rx="3" fill="none" stroke="var(--card-pink)" stroke-width="2"/>
        </svg>
        <svg viewBox="0 0 20 20" aria-label="Phone">
          <path d="M5 2.5 L8 2.5 L9 6.5 L7 8 C8 10.5 9.5 12 12 13 L13.5 11 L17.5 12 L17.5 15 C17.5 16.5 16.5 17.5 15 17.5 C8.5 17 3 11.5 2.5 5 C2.5 3.5 3.5 2.5 5 2.5 Z" fill="var(--card-pink)"/>
        </svg>
        <svg viewBox="0 0 20 20" aria-label="Website">
          <g fill="none" stroke="var(--card-pink)" stroke-width="1.6">
            <circle cx="10" cy="10" r="7.5"/>
            <ellipse cx="10" cy="10" rx="3.2" ry="7.5"/>
            <line x1="2.5" y1="10" x2="17.5" y2="10"/>
          </g>
        </svg>
      </div>
      <p class="contact__line">@lorna.tess.tresses__</p>
      <p class="contact__line">582 907 3365</p>
      <p class="contact__line">www.lornatesstresses.example</p>
    </div>
  </section>
</main>
</body>
</html>
```